Etiketten für Obsthof in Friedrichshafen am Bodensee
Zielgruppe
Wir sind ein Obsthof in Friedrichshafen am Bodensee und verkaufen in unserem Hofladen unsere selbsthergestellten Produkte. Dabei zeichnet uns besonders aus, dass wir unsere Produkte aus eigens angebautem Obst Herstellen wie zum Beispiel Marmeladen, Säfte, Sirup, Schnaps oder Liköre.
Unsere Zielgruppe sind Kundinnen und Kunden, die Wert auf Regionalität, Transparenz bei der Produktherstellung und Qualität der Inhaltsstoffe legen.
Aufgabenstellung
Uns ist besonders wichtig, dass die Etiketten widerspiegeln, dass die Produkte selbst hergestellt wurden und hochwertig sind.
Die Etiketten sollten alle auf einander abgestimmt sein, sodass sie sich wie eine klare Linie durch das ganze Sortiment ziehen. Dementsprechend soll ein universelles Etikett erstellt werden, das wir für alle unsere Produkte verwenden können. Hierbei ist es wichtig, dass wir im Nachhinein selbst die Produktbeschreibung auf dem Etikett an das jeweilige Produkt anpassen können.
Es sollte auch Platz sein für die Inhaltsstoffe, unsere Anschrift, Mindesthaltbarkeitsdatum und die Inhaltsmenge.
https://www.wendrahof-polmit.com/hofladen-und-produkte.htm
in diese Richtung könnte ich mir die Ausführung vorstellen.

```html
<!DOCTYPE html>
<html lang="de">
<head>
<meta charset="utf-8">
<title>Etiketten Obsthof Lindmar</title>
<link href="https://fonts.googleapis.com/css2?family=Montserrat:wght@400;500;600;700&family=Allura&display=swap" rel="stylesheet">
<style>
  :root {
    --green: #1f6b53;
    --green-dark: #1d5e49;
    --ink: #1a1a1a;
    --paper: #ffffff;
    --bg: #ffffff;
    --muted: #9a9a9a;
    --shadow: 0 1px 4px rgba(0,0,0,.12);
  }
  * { box-sizing: border-box; margin: 0; padding: 0; }
  html, body { width: 1091px; height: 1200px; overflow: hidden; background: var(--bg); }
  body { position: relative; font-family: "Montserrat", sans-serif; color: var(--green); }
  .swatches { position: absolute; top: 25px; right: 30px; display: flex; gap: 10px; }
  .swatch { width: 15px; height: 15px; }
  .swatch--green { background: var(--green); }
  .swatch--black { background: #000; }

  .tag { position: absolute; width: 170px; height: 170px; box-shadow: var(--shadow); }
  .tag__hole { position: absolute; top: 8px; right: 8px; width: 10px; height: 10px; border-radius: 50%; border: 1px solid #bbb; }
  .tag--front { left: 185px; top: 380px; background: var(--green); }
  .tag--front .tag__hole { border-color: #5f9a86; }
  .tag--back { left: 386px; top: 380px; background: var(--paper); padding: 14px 17px; }
  .tag__claim { font-size: 20px; line-height: 1.17; font-weight: 400; }
  .tag__web { position: absolute; left: 17px; bottom: 14px; font-size: 9.5px; }

  .note { position: absolute; left: 574px; top: 468px; width: 80px; height: 60px; }
  .note__text { position: absolute; left: 610px; top: 518px; font-size: 8.5px; letter-spacing: 1.5px; color: var(--muted); text-align: center; line-height: 1.5; }

  .label { position: absolute; background: var(--paper); border-top: 4px solid var(--green); box-shadow: var(--shadow); }
  .label--jar { left: 34px; top: 635px; width: 682px; height: 255px; }
  .label--bottle { left: 780px; top: 380px; width: 277px; height: 510px; text-align: center; }

  .wordmark { display: flex; align-items: center; justify-content: center; gap: 10px; }
  .wordmark__dot { width: 16px; height: 16px; border-radius: 50%; background: var(--green); }
  .wordmark__name { font-size: 30px; font-weight: 600; letter-spacing: 1px; color: var(--green); }

  .panel { position: absolute; top: 0; bottom: 0; text-align: center; color: var(--green-dark); }
  .panel--left { left: 12px; width: 150px; padding-top: 16px; }
  .panel--center { left: 220px; width: 242px; padding-top: 44px; }
  .panel--right { left: 520px; width: 150px; padding-top: 16px; }

  .heading { font-size: 10.5px; font-weight: 700; line-height: 1.05; }
  .body { font-size: 9.6px; line-height: 1.1; text-align: justify; text-align-last: center; margin-top: 12px; color: var(--green); }
  .rule { width: 48px; height: 2px; background: var(--green); margin: 16px auto 14px; }
  .script { font-family: "Allura", cursive; font-size: 19px; color: var(--green); line-height: 1; }
  .address { font-size: 9.6px; line-height: 1.12; margin-top: 10px; color: var(--green); }
  .kind { font-size: 13.5px; margin-top: 52px; color: var(--ink); }
  .product { font-size: 32px; line-height: 1.1; margin-top: 2px; }
  .claim { font-size: 13.5px; margin-top: 10px; color: var(--ink); }
  .mhd-label { font-size: 10px; font-weight: 700; margin-top: 14px; }
  .mhd-date { font-size: 11px; font-weight: 600; color: var(--ink); margin-top: 14px; }
  .amount { font-size: 22px; color: var(--green); }

  .label--bottle .wordmark { margin-top: 58px; }
  .label--bottle .product { font-size: 32px; line-height: 1.13; margin-top: 42px; }
  .label--bottle .claim { margin-top: 10px; color: var(--green); }
  .label--bottle .ingredients { font-size: 10px; margin-top: 32px; }
  .label--bottle .ingredients strong { display: block; font-weight: 700; }
  .label--bottle .rule { margin: 9px auto 16px; }
  .label--bottle .amount { margin-top: 14px; }

  .caption { position: absolute; top: 976px; left: 0; width: 1091px; text-align: center; font-size: 9px; letter-spacing: 1.6px; color: var(--muted); }
</style>
</head>
<body>
  <div class="swatches"><span class="swatch swatch--green"></span><span class="swatch swatch--black"></span></div>

  <div class="tag tag--front"><span class="tag__hole"></span></div>
  <div class="tag tag--back">
    <span class="tag__hole"></span>
    <p class="tag__claim">Produkte.<br>Frisch.<br>Regional.</p>
    <p class="tag__web">www.ferienhof-lindmar.de</p>
  </div>

  <svg class="note" viewBox="0 0 80 60" aria-hidden="true">
    <path d="M52 48 C40 28 22 22 4 20" fill="none" stroke="#333" stroke-width="1"/>
    <path d="M9 16 L3 20 L9 24" fill="none" stroke="#333" stroke-width="1"/>
  </svg>
  <p class="note__text">ANHÄNGER<br>40 MMM</p>

  <section class="label label--jar">
    <div class="panel panel--left">
      <p class="heading">Fruchtaufstrich<br>Himbeere</p>
      <p class="body">Lorem ipsum dolor sit amet, con setetur sadipscing elitr, sed diam nond aliquyam umaeirmod tempor invidunt uttad labore etedama ettade dolore magna aliquyam erat, sed diam voluptua. At vero eos et accusam et justo duo.</p>
      <div class="rule"></div>
      <p class="script">Qualität vom Bodensee</p>
      <p class="address">Obst- und Ferienhof Lindmar<br>Kirschweg 12<br>D-88099 Seefelden<br>www.ferienhof-lindmar.de</p>
    </div>
    <div class="panel panel--center">
      <div class="wordmark"><span class="wordmark__dot"></span><span class="wordmark__name">LINDMAR</span></div>
      <p class="kind">Fruchtaufstrich</p>
      <p class="product">Himbeere</p>
      <p class="claim">100% reine Frucht</p>
    </div>
    <div class="panel panel--right">
      <p class="heading">Zutaten:</p>
      <p class="body">Lorem ipsum dolor sit amet, con setetur sadipscing elitr, sed diam nond aliquyam umaeirmod tempor invidunt uttad labore etedama ettade dolore magna aliquyam erat, sed diam voluptua. At vero eos et accusam et justo duo dolores et ea rebum stet clita.</p>
      <p class="mhd-label">Mindestens haltbar bis:</p>
      <p class="mhd-date">14.08.2022</p>
      <div class="rule" style="margin:8px auto 14px"></div>
      <p class="amount">200 g ℮</p>
    </div>
  </section>

  <section class="label label--bottle">
    <div class="wordmark"><span class="wordmark__dot"></span><span class="wordmark__name">LINDMAR</span></div>
    <p class="product">Fruchtiger<br>Holunder-<br>blütensirup</p>
    <p class="claim">100% reine Frucht</p>
    <p class="ingredients"><strong>Zutaten:</strong>Wasser, Zucker, Holunderblüten</p>
    <p class="mhd-label">Mindestens haltbar bis:</p>
    <p class="mhd-date">14.08.2022</p>
    <div class="rule"></div>
    <p class="script">Qualität vom Bodensee</p>
    <p class="address" style="margin-top:6px">Obst- und Ferienhof Lindmar<br>Kirschweg 12 · D-88099 Seefelden<br>www.ferienhof-lindmar.de</p>
    <p class="amount">0,33 l ℮</p>
  </section>

  <p class="caption">ETIKETTEN „OBSTHOF LINDMAR“ ABMESSUNG 160 X 60 MM &amp; 65 X 120 MM · WWW.FERIENHOF-LINDMAR.DE</p>
</body>
</html>
```